Redesign of company powerpoint

I would like to redesign the attached powerpoint. Can you modernize it for me? Feel free to change the orders of the powerpoint slide. It is a selling document during this Coronavirus crisis. Need to highlight we have invested significantly to automate and modernize our factory

Target Market(s)

Multinational electronic companies

Requirements
Must have
• Appear to conservative multinational PCB buyers. Convey a sense of confidence and trust in the presentation.

```html
<!DOCTYPE html>
<html lang="en">
<head>
<meta charset="utf-8">
<title>KCG Company Presentation</title>
<link href="https://fonts.googleapis.com/css2?family=Montserrat:wght@400;500;600;700;800&family=Noto+Sans+SC:wght@400;700&display=swap" rel="stylesheet">
<style>
:root{
  --green-deep:#0a3d25;
  --green:#125a35;
  --green-mid:#1d7a46;
  --green-light:#3fa06a;
  --green-pale:#7cc59a;
  --mint:#d6ebdd;
  --grey:#e6e9e7;
  --grey-mid:#c4cbc6;
  --ink:#1c2a22;
  --muted:#68736c;
  --page:#f2f4f3;
  --white:#ffffff;
}
*{box-sizing:border-box;margin:0;padding:0}
html,body{width:1200px;height:2564px;overflow:hidden}
body{background:var(--page);font-family:"Montserrat","Noto Sans SC",sans-serif;color:var(--ink);position:relative}

/* tilted showcase */
.collage{position:absolute;left:205px;top:132px;width:790px;height:451px;display:grid;grid-template-columns:repeat(3,250px);grid-template-rows:repeat(3,141px);gap:14px 20px;transform:rotate(30deg) skewX(-30deg) scaleY(.864);transform-origin:center}
.cell{width:250px;height:141px;overflow:hidden;box-shadow:6px 8px 14px rgba(0,0,0,.22)}
.cell>.slide{transform:scale(.665);transform-origin:0 0;box-shadow:none}

/* slide grid */
.deck{position:absolute;left:16px;top:740px;display:grid;grid-template-columns:repeat(3,376px);grid-auto-rows:214px;gap:14px 20px}

.slide{position:relative;width:376px;height:214px;background:var(--white);overflow:hidden;box-shadow:0 2px 6px rgba(0,0,0,.13);padding:16px 18px 28px}
.slide--dark{background:linear-gradient(135deg,var(--green) 0%,var(--green-deep) 100%);color:var(--white)}
.slide::after{content:"";position:absolute;left:0;right:0;bottom:0;height:14px;background:var(--green-deep)}
.slide--dark::after{background:rgba(0,0,0,.28)}
.brand{position:absolute;left:12px;bottom:2px;z-index:2;font-size:8px;font-weight:800;color:var(--white);letter-spacing:.5px;display:flex;align-items:center;gap:4px}
.brand i{width:6px;height:6px;background:var(--green-light);display:block}

.title{font-size:13px;font-weight:700;color:var(--green);line-height:1.2}
.slide--dark .title{color:var(--white)}
.sub{font-size:7px;color:var(--muted);margin:2px 0 10px}
.slide--dark .sub{color:var(--mint)}
.txt{font-size:6.5px;line-height:1.55;color:var(--muted)}
.row{display:flex;gap:6px}
.box{background:var(--green);color:var(--white);font-size:7px;font-weight:600;padding:6px;flex:1;text-align:center}
.box--light{background:var(--grey);color:var(--ink)}
.box--mid{background:var(--green-mid)}
.bar{font-size:7px;font-weight:600;padding:6px 8px;margin-bottom:5px;color:var(--white);background:var(--green)}
.bar--mid{background:var(--green-mid)}
.bar--light{background:var(--grey);color:var(--ink)}

/* cover & divider */
.cover-name{font-size:22px;font-weight:800;line-height:1.1;text-align:center;margin-top:30px;letter-spacing:.5px}
.cover-line{width:150px;height:1px;background:var(--green-pale);margin:9px auto}
.cover-cn{text-align:center;font-size:8px;color:var(--mint)}
.divider-title{font-size:15px;font-weight:800;text-align:center;margin-top:66px;letter-spacing:1px}
.mission{font-size:11px;font-weight:600;line-height:1.45;margin-top:18px;width:240px}

/* photos (flat tone fills) */
.ph{background:linear-gradient(165deg,#dfe5e1,#9fa9a3)}
.ph--b{background:linear-gradient(160deg,#c8dccf,#5f8a70)}
.ph--c{background:linear-gradient(160deg,#9aa49e,#3f4944)}
.ph--d{background:linear-gradient(170deg,#eef1ef,#b8c3bc)}
.ph--e{background:linear-gradient(150deg,#b9c7bd,#6d7c73)}
.photos{display:grid;gap:5px;height:140px}
.photos--split{grid-template-columns:1.4fr 1fr;grid-template-rows:1fr 1fr}
.photos--split>:first-child{grid-row:1/3}
.photos--two{grid-template-columns:1fr 1fr}
.photos--three{grid-template-columns:repeat(3,1fr)}
.photos--full{height:170px;grid-template-columns:1fr 1fr 1fr;grid-template-rows:1fr 1fr}
.photos--full>:first-child{grid-column:1/3;grid-row:1/3}

/* misc */
.logos{display:grid;grid-template-columns:repeat(4,1fr);gap:5px 8px}
.logos span{font-size:8px;font-weight:700;color:var(--green);padding:8px 0;text-align:center;background:var(--page)}
.icon-grid{display:grid;grid-template-columns:repeat(3,1fr);gap:6px}
.icon-cell{background:var(--green);color:var(--white);text-align:center;font-size:6.5px;font-weight:600;padding:8px 4px}
.icon-cell svg{display:block;margin:0 auto 4px}
.icon-cell--mid{background:var(--green-mid)}
.list{font-size:6.5px;line-height:1.75;color:var(--ink);list-style:none}
.list li::before{content:"■ ";color:var(--green-mid)}
.badge{width:40px;height:30px;background:var(--grey);border-radius:3px}
.money{background:var(--green);color:var(--white);padding:5px 9px;margin-bottom:5px;width:150px}
.money small{display:block;font-size:6px;color:var(--mint)}
.money strong{font-size:11px}
.money--mid{background:var(--green-mid)}
.spec{border-collapse:collapse;font-size:6px;width:150px}
.spec td{border-bottom:1px solid var(--grey);padding:3px 2px}
.spec td:last-child{text-align:right;color:var(--green);font-weight:700}
.map{height:142px;background:linear-gradient(160deg,#e4eee8,#b9d3c3);position:relative}
.pin{position:absolute;left:58%;top:46%}
</style>
</head>
<body>

<section class="collage" aria-label="Featured slides">
  <div class="cell"><article class="slide slide--dark">
    <h2 class="title">Corporate Mission</h2><p class="sub">企业使命</p>
    <p class="mission">A premium low cost PCB manufacturer that fulfils customer, social and environmental responsibilities</p>
    <span class="brand"><i></i>KCG</span></article></div>
  <div class="cell"><article class="slide slide--dark">
    <p class="cover-name">KCG<br>INTERNATIONAL<br>LIMITED</p><div class="cover-line"></div>
    <p class="cover-cn">科尔顿电路集团有限公司</p><span class="brand"><i></i>KCG</span></article></div>
  <div class="cell"><article class="slide">
    <h2 class="title">Introduction to KCG</h2><p class="sub">公司简介</p>
    <div class="bar">Founded 1992 · Double sided &amp; multilayer PCB maker</div>
    <div class="bar bar--mid">Two plants · 1,200 staff · ISO certified</div>
    <div class="bar bar--light">Serving global electronics brands for 28 years</div>
    <span class="brand"><i></i>KCG</span></article></div>

  <div class="cell"><article class="slide">
    <h2 class="title">Main Customers</h2><p class="sub">主要客户</p>
    <div class="logos"><span>Arvex</span><span>Nordlan</span><span>Tessaro</span><span>Quinmark</span><span>Helion</span><span>Borvia</span><span>Castell</span><span>Lumetra</span></div>
    <span class="brand"><i></i>KCG</span></article></div>
  <div class="cell"><article class="slide">
    <h2 class="title">Competition Edges</h2><p class="sub">竞争优势</p>
    <div class="icon-grid">
      <div class="icon-cell">Cost</div><div class="icon-cell icon-cell--mid">Quality</div><div class="icon-cell">Delivery</div>
      <div class="icon-cell icon-cell--mid">Service</div><div class="icon-cell">Flexibility</div><div class="icon-cell icon-cell--mid">Technology</div>
    </div><span class="brand"><i></i>KCG</span></article></div>
  <div class="cell"><article class="slide">
    <h2 class="title">Factory Overview</h2><p class="sub">工厂概况</p>
    <div class="row" style="height:60px;margin-bottom:6px"><div class="box">30,000 m²<br>Area</div><div class="box box--mid">1,200<br>Staff</div><div class="box">60,000 m²<br>Monthly</div></div>
    <div class="row" style="height:40px"><div class="box box--mid">ISO 9001</div><div class="box">ISO 14001</div><div class="box box--mid">IATF 16949</div></div>
    <span class="brand"><i></i>KCG</span></article></div>

  <div class="cell"><article class="slide">
    <h2 class="title">Application</h2><p class="sub">产品应用</p>
    <div class="row" style="align-items:center;gap:24px">
      <svg width="150" height="100" viewBox="0 0 150 100" aria-label="Application bar chart"><rect y="4" width="130" height="10" fill="#125a35"/><rect y="24" width="100" height="10" fill="#1d7a46"/><rect y="44" width="76" height="10" fill="#3fa06a"/><rect y="64" width="52" height="10" fill="#7cc59a"/><rect y="84" width="30" height="10" fill="#c4cbc6"/></svg>
      <svg width="110" height="110" viewBox="0 0 32 32" aria-label="Application pie chart"><circle r="16" cx="16" cy="16" fill="#c4cbc6"/><circle r="8" cx="16" cy="16" fill="none" stroke="#125a35" stroke-width="16" stroke-dasharray="30 50.3" transform="rotate(-90 16 16)"/><circle r="8" cx="16" cy="16" fill="none" stroke="#3fa06a" stroke-width="16" stroke-dasharray="0 30 14 50.3" transform="rotate(-90 16 16)"/></svg>
    </div><span class="brand"><i></i>KCG</span></article></div>
  <div class="cell"><article class="slide slide--dark">
    <p class="divider-title">CONSTANT INVESTMENT</p><p class="cover-cn">持续投资</p><span class="brand"><i></i>KCG</span></article></div>
  <div class="cell"><article class="slide">
    <h2 class="title">2016–2020 Investments</h2><p class="sub">2016–2020 投资</p>
    <div class="row" style="gap:12px"><div><div class="money"><small>Automation</small><strong>USD 1.2 Million</strong></div><div class="money money--mid"><small>Equipment upgrade</small><strong>USD 2.4 Million</strong></div><div class="money"><small>Environmental</small><strong>USD 0.8 Million</strong></div></div>
    <div class="ph--b" role="img" aria-label="Automated production line" style="flex:1;height:118px"></div></div>
    <span class="brand"><i></i>KCG</span></article></div>
</section>

<section class="deck" aria-label="All slides">
  <article class="slide slide--dark">
    <p class="cover-name">KCG<br>INTERNATIONAL<br>LIMITED</p><div class="cover-line"></div>
    <p class="cover-cn">科尔顿电路集团有限公司</p><span class="brand"><i></i>KCG</span>
  </article>
  <article class="slide">
    <h2 class="title">Introduction to KCG</h2><p class="sub">公司简介</p>
    <div class="bar">Founded 1992 · Double sided &amp; multilayer PCB maker</div>
    <div class="bar bar--mid">Two plants · 1,200 staff · ISO certified</div>
    <div class="bar bar--light">Serving global electronics brands for 28 years</div>
    <p class="txt">Export focused supplier to Europe, America and Asia with stable quality and delivery.</p>
    <span class="brand"><i></i>KCG</span>
  </article>
  <article class="slide">
    <h2 class="title">Shareholder Structure</h2><p class="sub">股东结构</p>
    <svg width="340" height="120" viewBox="0 0 340 120" aria-label="Shareholder chart">
      <rect x="115" y="4" width="110" height="26" fill="#125a35"/><text x="170" y="21" fill="#fff" font-size="8" font-weight="700" text-anchor="middle" font-family="Montserrat,sans-serif">KCG Holdings</text>
      <path d="M170 30V50M70 50H270M70 50V64M270 50V64" stroke="#125a35" fill="none"/>
      <rect x="15" y="64" width="110" height="26" fill="#1d7a46"/><text x="70" y="81" fill="#fff" font-size="8" font-weight="600" text-anchor="middle" font-family="Montserrat,sans-serif">Plant A · 100%</text>
      <rect x="215" y="64" width="110" height="26" fill="#1d7a46"/><text x="270" y="81" fill="#fff" font-size="8" font-weight="600" text-anchor="middle" font-family="Montserrat,sans-serif">Plant B · 100%</text>
    </svg>
    <span class="brand"><i></i>KCG</span>
  </article>

  <article class="slide slide--dark">
    <h2 class="title">Corporate Mission</h2><p class="sub">企业使命</p>
    <p class="mission">A premium low cost PCB manufacturer that fulfils customer, social and environmental responsibilities</p>
    <span class="brand"><i></i>KCG</span>
  </article>
  <article class="slide">
    <h2 class="title">KCG Business Principles</h2><p class="sub">经营原则</p>
    <div class="row" style="height:66px"><div class="box box--light">Quality First</div><div class="box">Customer Focus</div><div class="box box--mid">Continuous Improvement</div></div>
    <div class="bar" style="margin-top:8px">KCG builds long term partnerships through consistent delivery.</div>
    <span class="brand"><i></i>KCG</span>
  </article>
  <article class="slide">
    <h2 class="title">Competition Edges</h2><p class="sub">竞争优势</p>
    <div class="icon-grid">
      <div class="icon-cell"><svg width="14" height="14" viewBox="0 0 14 14"><circle cx="7" cy="7" r="6" fill="none" stroke="#fff"/></svg>Cost</div>
      <div class="icon-cell icon-cell--mid"><svg width="14" height="14" viewBox="0 0 14 14"><path d="M2 7l3 3 7-7" fill="none" stroke="#fff" stroke-width="1.6"/></svg>Quality</div>
      <div class="icon-cell"><svg width="14" height="14" viewBox="0 0 14 14"><path d="M1 7h10M8 3l4 4-4 4" fill="none" stroke="#fff" stroke-width="1.4"/></svg>Delivery</div>
      <div class="icon-cell icon-cell--mid"><svg width="14" height="14" viewBox="0 0 14 14"><circle cx="7" cy="7" r="6" fill="none" stroke="#fff"/></svg>Service</div>
      <div class="icon-cell"><svg width="14" height="14" viewBox="0 0 14 14"><rect x="2" y="2" width="10" height="10" fill="none" stroke="#fff"/></svg>Flexibility</div>
      <div class="icon-cell icon-cell--mid"><svg width="14" height="14" viewBox="0 0 14 14"><rect x="2" y="2" width="10" height="10" fill="none" stroke="#fff"/></svg>Technology</div>
    </div>
    <span class="brand"><i></i>KCG</span>
  </article>

  <article class="slide">
    <h2 class="title">Factory Location</h2><p class="sub">工厂位置</p>
    <div class="map" role="img" aria-label="Regional map showing the factory location">
      <svg class="pin" width="16" height="20" viewBox="0 0 16 20"><path d="M8 19C3 12 1 9 1 7a7 7 0 0114 0c0 2-2 5-7 12z" fill="#125a35"/><circle cx="8" cy="7" r="2.5" fill="#fff"/></svg>
    </div>
    <span class="brand"><i></i>KCG</span>
  </article>
  <article class="slide">
    <h2 class="title">Factory Overview</h2><p class="sub">工厂概况</p>
    <div class="row" style="height:64px;margin-bottom:6px"><div class="box">30,000 m²<br>Area</div><div class="box box--mid">1,200<br>Staff</div><div class="box">60,000 m²<br>Monthly</div></div>
    <div class="row" style="height:44px"><div class="box box--mid">ISO 9001</div><div class="box">ISO 14001</div><div class="box box--mid">IATF 16949</div></div>
    <span class="brand"><i></i>KCG</span>
  </article>
  <article class="slide">
    <h2 class="title">Organization Structure</h2><p class="sub">组织架构</p>
    <svg width="340" height="120" viewBox="0 0 340 120" aria-label="Organization chart">
      <rect x="125" y="2" width="90" height="20" fill="#125a35"/>
      <path d="M170 22V36M32 36H308" stroke="#125a35" fill="none"/>
      <g fill="#1d7a46"><rect x="4" y="42" width="56" height="20"/><rect x="73" y="42" width="56" height="20"/><rect x="142" y="42" width="56" height="20"/><rect x="211" y="42" width="56" height="20"/><rect x="280" y="42" width="56" height="20"/></g>
      <g fill="#d6ebdd"><rect x="4" y="70" width="56" height="16"/><rect x="73" y="70" width="56" height="16"/><rect x="142" y="70" width="56" height="16"/><rect x="211" y="70" width="56" height="16"/><rect x="280" y="70" width="56" height="16"/><rect x="4" y="92" width="56" height="16"/><rect x="142" y="92" width="56" height="16"/><rect x="280" y="92" width="56" height="16"/></g>
    </svg>
    <span class="brand"><i></i>KCG</span>
  </article>

  <article class="slide">
    <h2 class="title">Main Customers</h2><p class="sub">主要客户</p>
    <div class="logos">
      <span>Arvex</span><span>Nordlan</span><span>Tessaro</span><span>Quinmark</span>
      <span>Helion</span><span>Borvia</span><span>Castell</span><span>Lumetra</span>
      <span>Orvane</span><span>Pexley</span><span>Rinmoor</span><span>Sylvex</span>
    </div>
    <span class="brand"><i></i>KCG</span>
  </article>
  <article class="slide">
    <h2 class="title">Application</h2><p class="sub">产品应用</p>
    <div class="row" style="align-items:center;gap:24px">
      <svg width="150" height="100" viewBox="0 0 150 100" aria-label="Application bar chart"><rect y="4" width="130" height="10" fill="#125a35"/><rect y="24" width="100" height="10" fill="#1d7a46"/><rect y="44" width="76" height="10" fill="#3fa06a"/><rect y="64" width="52" height="10" fill="#7cc59a"/><rect y="84" width="30" height="10" fill="#c4cbc6"/></svg>
      <svg width="110" height="110" viewBox="0 0 32 32" aria-label="Application pie chart"><circle r="16" cx="16" cy="16" fill="#c4cbc6"/><circle r="8" cx="16" cy="16" fill="none" stroke="#125a35" stroke-width="16" stroke-dasharray="30 50.3" transform="rotate(-90 16 16)"/><circle r="8" cx="16" cy="16" fill="none" stroke="#3fa06a" stroke-width="16" stroke-dasharray="0 30 14 50.3" transform="rotate(-90 16 16)"/></svg>
    </div>
    <span class="brand"><i></i>KCG</span>
  </article>
  <article class="slide">
    <h2 class="title">Key Capabilities</h2><p class="sub">制程能力</p>
    <div class="row" style="gap:18px">
      <ul class="list"><li>Layer count: 1 – 12 layers</li><li>Board thickness: 0.4 – 3.2 mm</li><li>Min. line / space: 3 / 3 mil</li><li>Min. drill hole: 0.2 mm</li><li>Finish: HASL, ENIG, OSP</li><li>Copper weight: 0.5 – 4 oz</li></ul>
      <table class="spec"><tr><td>Max panel size</td><td>600×500</td></tr><tr><td>Aspect ratio</td><td>10:1</td></tr><tr><td>Impedance</td><td>±10%</td></tr><tr><td>Bow &amp; twist</td><td>≤0.75%</td></tr><tr><td>Solder mask</td><td>4 colours</td></tr></table>
    </div>
    <span class="brand"><i></i>KCG</span>
  </article>

  <article class="slide">
    <h2 class="title">Laminates With UL</h2><p class="sub">UL 认证板材</p>
    <div class="row" style="gap:18px">
      <ul class="list"><li>FR-4 standard Tg</li><li>FR-4 high Tg</li><li>CEM-1 / CEM-3</li><li>Aluminium base</li><li>Halogen free</li></ul>
      <div style="display:grid;grid-template-columns:repeat(3,40px);gap:8px"><div class="badge"></div><div class="badge"></div><div class="badge"></div><div class="badge"></div><div class="badge"></div><div class="badge"></div></div>
    </div>
    <span class="brand"><i></i>KCG</span>
  </article>
  <article class="slide">
    <h2 class="title">Screen printing ink</h2><p class="sub">油墨</p>
    <div class="row" style="gap:10px;margin-top:6px"><div class="badge"></div><div class="badge"></div><div class="badge"></div><div class="ph--b" role="img" aria-label="Ink containers" style="flex:1;height:70px"></div></div>
    <p class="txt" style="margin-top:10px">UL listed solder mask and legend inks in green, black, white and blue.</p>
    <span class="brand"><i></i>KCG</span>
  </article>
  <article class="slide slide--dark">
    <p class="divider-title">CONSTANT INVESTMENT</p><p class="cover-cn">持续投资</p>
    <span class="brand"><i></i>KCG</span>
  </article>

  <article class="slide">
    <h2 class="title">2016–2020 Investments</h2><p class="sub">2016–2020 投资</p>
    <div class="row" style="gap:12px"><div><div class="money"><small>Automation</small><strong>USD 1.2 Million</strong></div><div class="money money--mid"><small>Equipment upgrade</small><strong>USD 2.4 Million</strong></div><div class="money"><small>Environmental</small><strong>USD 0.8 Million</strong></div></div>
    <div class="ph--b" role="img" aria-label="Automated production line" style="flex:1;height:118px"></div></div>
    <span class="brand"><i></i>KCG</span>
  </article>
  <article class="slide">
    <h2 class="title">Automatic Screen Printing Line</h2><p class="sub">自动丝印线</p>
    <div class="photos photos--split"><div class="ph--c" role="img" aria-label="Automatic screen printing machine"></div><div class="ph" role="img" aria-label="Printing head"></div><div class="ph--b" role="img" aria-label="Printed panels"></div></div>
    <span class="brand"><i></i>KCG</span>
  </article>
  <article class="slide">
    <h2 class="title">Slotting Line</h2><p class="sub">开槽线</p>
    <div class="photos photos--two"><div class="ph--d" role="img" aria-label="Slotting line equipment"></div><div class="ph--e" role="img" aria-label="Slotting line workstation"></div></div>
    <span class="brand"><i></i>KCG</span>
  </article>

  <article class="slide">
    <h2 class="title">Automatic HASL Line</h2><p class="sub">自动喷锡线</p>
    <div class="photos photos--split"><div class="ph" role="img" aria-label="Automatic hot air solder levelling line"></div><div class="ph--c" role="img" aria-label="HASL control panel"></div><div class="ph--e" role="img" aria-label="Finished boards"></div></div>
    <span class="brand"><i></i>KCG</span>
  </article>
  <article class="slide">
    <h2 class="title">Vanter CNC Drill</h2><p class="sub">数控钻机</p>
    <div class="photos photos--two"><div class="ph--d" role="img" aria-label="CNC drilling machines in a row"></div><div class="ph--b" role="img" aria-label="CNC drill close up"></div></div>
    <span class="brand"><i></i>KCG</span>
  </article>
  <article class="slide">
    <h2 class="title">Guiding Hole Punching Machine</h2><p class="sub">定位孔冲孔机</p>
    <div class="photos photos--split"><div class="ph--d" role="img" aria-label="Guiding hole punching machine"></div><div class="ph--c" role="img" aria-label="Machine display screen"></div><div class="ph" role="img" aria-label="Punched panels"></div></div>
    <span class="brand"><i></i>KCG</span>
  </article>

  <article class="slide">
    <h2 class="title">CCD punching</h2><p class="sub">CCD 冲孔</p>
    <div class="photos photos--two"><div class="ph--e" role="img" aria-label="CCD punching machine"></div><div class="ph--d" role="img" aria-label="CCD punching work area"></div></div>
    <span class="brand"><i></i>KCG</span>
  </article>
  <article class="slide">
    <div class="photos photos--full"><div class="ph--b" role="img" aria-label="Production floor"></div><div class="ph" role="img" aria-label="Inspection equipment"></div><div class="ph--c" role="img" aria-label="Plating line"></div></div>
    <span class="brand"><i></i>KCG</span>
  </article>
  <article class="slide">
    <div class="photos photos--full"><div class="ph--d" role="img" aria-label="Electrical testing station"></div><div class="ph--e" role="img" aria-label="Automated conveyor"></div><div class="ph--b" role="img" aria-label="Packing area"></div></div>
    <span class="brand"><i></i>KCG</span>
  </article>
</section>

</body>
</html>
```